body balm label design

body balm tube design, current label design for other similar products
Need to have a design which can interchange between 3 different solutions
Quiet Orchard (Lavender + Vanilla)
Copper Trail (Eucalyptus + Mint)
Fern Hollow (Bergamot + Cedarwood)
Tube size:
2.5h x 3.25 w
Target Market(s)
natural, solution focused
Requirements
Must have
- relatable to existing brand designs, focus on features and benefits

```html
<!DOCTYPE html>
<html lang="en">
<head>
<meta charset="utf-8">
<title>Body balm labels</title>
<link rel="stylesheet" href="https://fonts.googleapis.com/css2?family=Cormorant+Garamond:wght@500&family=Great+Vibes&family=Open+Sans:wght@400;600&display=swap">
<style>
  :root {
    --bg-top: #dcd8e8;
    --bg-bottom: #ece9f3;
    --label: #ffffff;
    --ink: #333333;
    --ink-soft: #444444;
    --bar: #58585a;
    --lavender: #8a86b8;
    --eucalyptus: #c2d582;
    --bergamot: #f27c57;
    --bergamot-light: #f9b7a0;
  }
  * { box-sizing: border-box; margin: 0; padding: 0; }
  html, body { width: 1200px; height: 960px; overflow: hidden; }
  body {
    background: linear-gradient(180deg, var(--bg-top), var(--bg-bottom));
    font-family: "Open Sans", sans-serif;
    color: var(--ink);
  }
  .canvas {
    position: relative;
    width: 1200px;
    height: 960px;
  }
  .label {
    position: absolute;
    top: 180px;
    width: 300px;
    height: 600px;
    background: var(--label);
    box-shadow: 0 6px 24px rgba(90, 80, 130, 0.12);
    overflow: hidden;
  }
  .label--orchard { left: 115px; --accent: var(--lavender); }
  .label--trail   { left: 450px; --accent: var(--eucalyptus); }
  .label--hollow  { left: 785px; --accent: var(--bergamot); }

  .label__dot {
    position: absolute;
    top: 0; left: 106px;
    width: 88px; height: 44px;
    border-radius: 0 0 44px 44px;
    background: var(--accent);
  }
  .label__title {
    position: absolute;
    top: 74px; left: 0; right: 0;
    text-align: center;
    font-family: "Cormorant Garamond", serif;
    font-weight: 500;
    font-size: 29px;
    letter-spacing: 0.08em;
    text-transform: uppercase;
    color: var(--ink);
  }
  .label__rule {
    position: absolute;
    top: 138px; left: 36px;
    width: 86px; height: 1px;
    background: var(--ink);
  }
  .label__kind {
    position: absolute;
    top: 110px; left: 128px;
    font-family: "Great Vibes", cursive;
    font-size: 34px;
    color: var(--ink);
  }
  .label__frame {
    position: absolute;
    top: 185px; left: 62px;
    width: 176px; height: 305px;
    border: 2px solid var(--accent);
    border-bottom: none;
  }
  .label__art {
    position: absolute;
    opacity: 0.85;
  }
  .label__art--top {
    top: 150px; left: 18px;
    width: 66px; height: 190px;
    border-radius: 50% 50% 40% 40%;
    background: radial-gradient(ellipse at 50% 30%, var(--accent), rgba(255,255,255,0) 72%);
  }
  .label__art--side {
    top: 240px; left: 180px;
    width: 76px; height: 250px;
    border-radius: 45%;
    background: radial-gradient(ellipse at 50% 50%, var(--accent), rgba(255,255,255,0) 70%);
  }
  .label--trail .label__art--top { top: 160px; height: 140px; }
  .label--trail .label__art--side { top: 330px; height: 170px; left: 170px; }
  .label--hollow .label__art--top { top: 240px; height: 170px; left: 14px; }
  .label--hollow .label__art--side { top: 280px; height: 200px; }

  .features {
    position: absolute;
    top: 204px; left: 62px;
    width: 176px;
    list-style: none;
    text-align: center;
    font-size: 10.5px;
    line-height: 16px;
    letter-spacing: 0.22em;
    color: var(--ink-soft);
  }
  .features li { position: absolute; left: 0; right: 0; }
  .features li:nth-child(1) { top: 0; }
  .features li:nth-child(2) { top: 70px; }
  .features li:nth-child(3) { top: 130px; }
  .features li:nth-child(4) { top: 209px; }
  .features .dash {
    position: absolute;
    left: 73px; width: 30px; height: 1px;
    background: var(--ink-soft);
  }
  .dash--1 { top: 48px; }
  .dash--2 { top: 109px; }
  .dash--3 { top: 188px; }

  .spec {
    position: absolute;
    top: 490px; left: 62px;
    width: 176px; height: 16px;
    display: flex; gap: 2px;
  }
  .spec span {
    flex: 1;
    background: var(--bar);
    color: #ffffff;
    font-size: 8px;
    font-weight: 600;
    letter-spacing: 0.08em;
    line-height: 16px;
    text-align: center;
  }
  .scent {
    position: absolute;
    top: 508px; left: 62px;
    width: 176px; height: 52px;
    background: var(--accent);
    color: #ffffff;
    text-align: center;
    font-size: 14px;
    line-height: 17px;
    letter-spacing: 0.3em;
    padding-top: 9px;
  }
  .label--hollow .scent {
    background: linear-gradient(90deg, var(--bergamot), var(--bergamot-light));
    font-weight: 600;
    letter-spacing: 0.2em;
  }
</style>
</head>
<body>
<main class="canvas">

  <article class="label label--orchard">
    <div class="label__dot"></div>
    <h2 class="label__title">Quiet Orchard</h2>
    <div class="label__rule"></div>
    <p class="label__kind">Body balm</p>
    <div class="label__frame"></div>
    <div class="label__art label__art--top" role="img" aria-label="Line drawing of a wild flower in lavender purple"></div>
    <div class="label__art label__art--side" role="img" aria-label="Line drawing of lavender sprigs in purple"></div>
    <ul class="features">
      <li>100% natural<br>plant based</li>
      <li>handpoured</li>
      <li>gently<br>scented</li>
      <li>eco<br>friendly</li>
      <span class="dash dash--1"></span><span class="dash dash--2"></span><span class="dash dash--3"></span>
    </ul>
    <div class="spec"><span>500 ml</span><span>organic</span></div>
    <p class="scent">lavender<br>+ vanilla</p>
  </article>

  <article class="label label--trail">
    <div class="label__dot"></div>
    <h2 class="label__title">Copper Trail</h2>
    <div class="label__rule"></div>
    <p class="label__kind">Body balm</p>
    <div class="label__frame"></div>
    <div class="label__art label__art--top" role="img" aria-label="Line drawing of a eucalyptus branch in soft green"></div>
    <div class="label__art label__art--side" role="img" aria-label="Line drawing of mint leaves in soft green"></div>
    <ul class="features">
      <li>100% natural<br>plant based</li>
      <li>handpoured</li>
      <li>gently<br>scented</li>
      <li>eco<br>friendly</li>
      <span class="dash dash--1"></span><span class="dash dash--2"></span><span class="dash dash--3"></span>
    </ul>
    <div class="spec"><span>500 ml</span><span>organic</span></div>
    <p class="scent">eucalyptus<br>+ mint</p>
  </article>

  <article class="label label--hollow">
    <div class="label__dot"></div>
    <h2 class="label__title">Fern Hollow</h2>
    <div class="label__rule"></div>
    <p class="label__kind">Body balm</p>
    <div class="label__frame"></div>
    <div class="label__art label__art--top" role="img" aria-label="Drawing of bergamot blossoms in coral orange"></div>
    <div class="label__art label__art--side" role="img" aria-label="Drawing of cedar cones and foliage fading to peach"></div>
    <ul class="features">
      <li>100% natural<br>plant based</li>
      <li>handpoured</li>
      <li>gently<br>scented</li>
      <li>eco<br>friendly</li>
      <span class="dash dash--1"></span><span class="dash dash--2"></span><span class="dash dash--3"></span>
    </ul>
    <div class="spec"><span>500 ml</span><span>organic</span></div>
    <p class="scent">Bergamot<br>+ Cedarwood</p>
  </article>

</main>
</body>
</html>
```